Funny (Jokebin-alike) Site Design + Code Needed

Hello everybody,

I'm newcomer who want to make a site that could generate income in the future.
I'm interested in funny photo sites like jokebin.
So I need:

- An website that works like jokebin (users post images, comments...)
- The website should have ability to crawl images from jokebin posts then post in my site(every x min/hrs)...
- The web graphic should be design to be clean, fresh, neat as well as there are spots for ads.

In sum, I need an autopilot jokebin-alike site.
I think there are alot of source that looks like jokebin. So the main point here is to design it unique, and make it autopilot.

Any question, please inbox me.
Thanks.

```html
<!DOCTYPE html>
<html lang="en">
<head>
<meta charset="utf-8">
<title>Giggle Nest</title>
<link rel="stylesheet" href="https://fonts.googleapis.com/css2?family=Bebas+Neue&family=Oswald:wght@400;500&display=swap">
<style>
:root{
  --ink:#1c1c1c;
  --page:#e9e9e9;
  --card:#ffffff;
  --teal:#1bb5b2;
  --heading:#15655f;
  --text:#333333;
  --soft-teal:#7fdad7;
}
*{margin:0;padding:0;box-sizing:border-box}
html,body{width:1200px;height:2503px;overflow:hidden}
body{background:var(--page) repeating-linear-gradient(45deg,rgba(0,0,0,.025) 0 2px,transparent 2px 6px);font-family:"Oswald",sans-serif;color:var(--text);position:relative}

.site-header{position:absolute;left:0;top:0;width:1200px;height:113px;background:var(--ink)}
.brand{position:absolute;left:130px;top:38px;font-family:"Oswald",sans-serif;font-weight:500;font-size:36px;line-height:1;color:#ffffff;letter-spacing:1px}
.main-nav{position:absolute;top:64px;font-family:"Bebas Neue",sans-serif;font-size:20px;color:#fff;letter-spacing:.5px}
.account{position:absolute;top:67px;font-family:"Bebas Neue",sans-serif;font-size:15px;color:#fff}
.account-sep{position:absolute;top:66px;width:1px;height:16px;background:#aaa}
.upload-btn{position:absolute;left:978px;top:63px;width:60px;height:22px;background:var(--teal);color:#fff;font-family:"Bebas Neue",sans-serif;font-size:15px;text-align:center;line-height:23px}
.gear{position:absolute;left:1053px;top:62px}
.search{position:absolute;left:893px;top:20px;width:180px;height:18px;background:#f2f2f2;border:1px solid #bbb;font-size:9px;color:#999;padding-left:6px;line-height:16px}
.search svg{position:absolute;right:4px;top:4px}

.content{position:absolute;left:112px;top:113px;width:961px;height:2282px;background:var(--card);border:1px solid #e2e2e2}

.post{position:absolute;left:132px;width:619px}
.post-head{display:flex;justify-content:space-between;align-items:center;height:27px}
.post-title{font-family:"Bebas Neue",sans-serif;font-size:17px;color:var(--text);letter-spacing:.3px}
.post-date{font-family:"Bebas Neue",sans-serif;font-size:13px;color:var(--text)}
.post-media{width:619px;height:305px;display:block}
.share-bar{position:relative;height:53px;background:var(--teal);color:#fff}
.share-label{position:absolute;left:17px;top:18px;font-family:"Bebas Neue",sans-serif;font-size:16px;line-height:1}
.share-icon{position:absolute;top:15px;width:23px;height:23px;border-radius:2px}
.comment-link{position:absolute;left:344px;top:14px}
.comment-label{position:absolute;left:377px;top:19px;font-family:"Bebas Neue",sans-serif;font-size:14px;line-height:1;color:var(--soft-teal)}
.share-count{position:absolute;right:22px;top:15px;font-family:"Bebas Neue",sans-serif;font-size:22px;line-height:1}

.ad{position:absolute;width:300px;height:250px}
.side-heading{position:absolute;left:769px;font-family:"Bebas Neue",sans-serif;font-size:28px;font-weight:400;color:var(--heading);letter-spacing:.3px}
.thumb-item{position:absolute;left:769px;width:300px;height:100px}
.thumb{position:absolute;left:0;top:0;width:113px;height:100px}
.thumb-title{position:absolute;left:125px;top:33px;font-family:"Bebas Neue",sans-serif;font-size:16px;color:var(--text)}
.thumb-date{position:absolute;left:125px;top:58px;font-family:"Bebas Neue",sans-serif;font-size:16px;color:var(--heading)}
.view-more{position:absolute;left:981px;width:82px;height:30px;background:var(--teal);color:#fff;font-family:"Bebas Neue",sans-serif;font-size:15px;text-align:center;line-height:31px}
.store-badge{position:absolute;left:771px;width:148px;height:52px;background:#000;border:2px solid #999;border-radius:6px}

.pager{position:absolute;top:2330px;left:298px;display:flex;gap:9px}
.pager span{display:block;height:30px;min-width:29px;padding:0 8px;background:#f2f2f2;border:1px solid #d5d5d5;font-family:"Bebas Neue",sans-serif;font-size:16px;line-height:30px;text-align:center;color:#444}
.pager .wide{min-width:50px}

.site-footer{position:absolute;left:0;top:2420px;width:1200px;text-align:center;font-family:"Bebas Neue",sans-serif;color:var(--ink)}
.footer-nav{font-size:17px}
.copyright{font-size:15px;margin-top:10px}
</style>
</head>
<body>

<header class="site-header">
  <div class="brand">GIGGLE NEST</div>
  <div class="search">SEARCH<svg width="8" height="8" viewBox="0 0 8 8"><circle cx="3" cy="3" r="2.2" fill="none" stroke="#999"/><line x1="4.6" y1="4.6" x2="7.5" y2="7.5" stroke="#999"/></svg></div>
  <nav>
    <span class="main-nav" style="left:447px">HOME</span>
    <span class="main-nav" style="left:506px">ABOUT US</span>
    <span class="main-nav" style="left:588px">SHARE</span>
    <span class="main-nav" style="left:649px">POST IMAGES</span>
    <span class="main-nav" style="left:756px">COMMENTS</span>
  </nav>
  <span class="account" style="left:871px">LOGIN</span>
  <span class="account-sep" style="left:914px"></span>
  <span class="account" style="left:926px">SIGNUP</span>
  <span class="account-sep" style="left:967px"></span>
  <span class="upload-btn">UPLOAD</span>
  <svg class="gear" width="24" height="24" viewBox="0 0 24 24"><g fill="#fff"><circle cx="12" cy="12" r="7"/><rect x="10" y="1" width="4" height="22"/><rect x="1" y="10" width="22" height="4"/><rect x="10" y="1" width="4" height="22" transform="rotate(45 12 12)"/><rect x="10" y="1" width="4" height="22" transform="rotate(-45 12 12)"/></g><circle cx="12" cy="12" r="3.2" fill="#1c1c1c"/></svg>
</header>

<main class="content"></main>

<article class="post" style="top:170px">
  <div class="post-head"><span class="post-title">NEQUE PORRO QUIS QUAMEST QUI DO LOREM</span><span class="post-date">POSTED ON: 23-10-2013</span></div>
  <div class="post-media" role="img" aria-label="Photo of fruit stall with strawberries and grapes" style="background:linear-gradient(160deg,#7a8a2a,#b5261c 45%,#5a1414 75%,#2a1a18)"></div>
  <div class="share-bar">
    <span class="share-label">SHARE US WITH</span>
    <span class="share-icon" style="left:133px;background:#55acee"></span>
    <span class="share-icon" style="left:167px;background:#cb2027"></span>
    <span class="share-icon" style="left:201px;background:#3b5998"></span>
    <span class="share-icon" style="left:235px;background:#555"></span>
    <span class="share-icon" style="left:269px;background:#e52d27"></span>
    <span class="share-icon" style="left:303px;background:#f29a1d"></span>
    <svg class="comment-link" width="26" height="22" viewBox="0 0 26 22"><path d="M2 2h22v13H10l-5 5v-5H2z" fill="#fff"/></svg>
    <span class="comment-label">COMMENTS</span>
    <span class="share-count">1520 SHARES</span>
  </div>
</article>

<article class="post" style="top:610px">
  <div class="post-head"><span class="post-title">NEQUE PORRO QUIS QUAMEST QUI DO LOREM</span><span class="post-date">POSTED ON: 23-10-2013</span></div>
  <div class="post-media" role="img" aria-label="Photo of a marina with sailboats and palm trees" style="background:linear-gradient(180deg,#3f8fd8,#8cc2ea 40%,#2fb0b0 65%,#2f6a3a)"></div>
  <div class="share-bar">
    <span class="share-label">SHARE US WITH</span>
    <span class="share-icon" style="left:133px;background:#55acee"></span>
    <span class="share-icon" style="left:167px;background:#cb2027"></span>
    <span class="share-icon" style="left:201px;background:#3b5998"></span>
    <span class="share-icon" style="left:235px;background:#555"></span>
    <span class="share-icon" style="left:269px;background:#e52d27"></span>
    <span class="share-icon" style="left:303px;background:#f29a1d"></span>
    <svg class="comment-link" width="26" height="22" viewBox="0 0 26 22"><path d="M2 2h22v13H10l-5 5v-5H2z" fill="#fff"/></svg>
    <span class="comment-label">COMMENTS</span>
    <span class="share-count">1520 SHARES</span>
  </div>
</article>

<article class="post" style="top:1051px">
  <div class="post-head"><span class="post-title">NEQUE PORRO QUIS QUAMEST QUI DO LOREM</span><span class="post-date">POSTED ON: 23-10-2013</span></div>
  <div class="post-media" role="img" aria-label="Photo of a busy city street with pedestrians and cyclists" style="background:linear-gradient(180deg,#a9bfd6,#9a4f44 35%,#6e6a66 70%,#555)"></div>
  <div class="share-bar">
    <span class="share-label">SHARE US WITH</span>
    <span class="share-icon" style="left:133px;background:#55acee"></span>
    <span class="share-icon" style="left:167px;background:#cb2027"></span>
    <span class="share-icon" style="left:201px;background:#3b5998"></span>
    <span class="share-icon" style="left:235px;background:#555"></span>
    <span class="share-icon" style="left:269px;background:#e52d27"></span>
    <span class="share-icon" style="left:303px;background:#f29a1d"></span>
    <svg class="comment-link" width="26" height="22" viewBox="0 0 26 22"><path d="M2 2h22v13H10l-5 5v-5H2z" fill="#fff"/></svg>
    <span class="comment-label">COMMENTS</span>
    <span class="share-count">1520 SHARES</span>
  </div>
</article>

<article class="post" style="top:1490px">
  <div class="post-head"><span class="post-title">NEQUE PORRO QUIS QUAMEST QUI DO LOREM</span><span class="post-date">POSTED ON: 23-10-2013</span></div>
  <div class="post-media" role="img" aria-label="Photo of a wine bottle and glass at a vineyard sunset" style="background:linear-gradient(180deg,#d9c070,#f2e6a8 35%,#c8a040 65%,#4a3a18)"></div>
  <div class="share-bar">
    <span class="share-label">SHARE US WITH</span>
    <span class="share-icon" style="left:133px;background:#55acee"></span>
    <span class="share-icon" style="left:167px;background:#cb2027"></span>
    <span class="share-icon" style="left:201px;background:#3b5998"></span>
    <span class="share-icon" style="left:235px;background:#555"></span>
    <span class="share-icon" style="left:269px;background:#e52d27"></span>
    <span class="share-icon" style="left:303px;background:#f29a1d"></span>
    <svg class="comment-link" width="26" height="22" viewBox="0 0 26 22"><path d="M2 2h22v13H10l-5 5v-5H2z" fill="#fff"/></svg>
    <span class="comment-label">COMMENTS</span>
    <span class="share-count">1520 SHARES</span>
  </div>
</article>

<article class="post" style="top:1927px">
  <div class="post-head"><span class="post-title">NEQUE PORRO QUIS QUAMEST QUI DO LOREM</span><span class="post-date">POSTED ON: 23-10-2013</span></div>
  <div class="post-media" role="img" aria-label="Photo of a person meditating on a mountain at sunrise" style="background:linear-gradient(170deg,#c03a8a,#f0a0a0 35%,#e07840 65%,#5a2010)"></div>
  <div class="share-bar">
    <span class="share-label">SHARE US WITH</span>
    <span class="share-icon" style="left:133px;background:#55acee"></span>
    <span class="share-icon" style="left:167px;background:#cb2027"></span>
    <span class="share-icon" style="left:201px;background:#3b5998"></span>
    <span class="share-icon" style="left:235px;background:#555"></span>
    <span class="share-icon" style="left:269px;background:#e52d27"></span>
    <span class="share-icon" style="left:303px;background:#f29a1d"></span>
    <svg class="comment-link" width="26" height="22" viewBox="0 0 26 22"><path d="M2 2h22v13H10l-5 5v-5H2z" fill="#fff"/></svg>
    <span class="comment-label">COMMENTS</span>
    <span class="share-count">1520 SHARES</span>
  </div>
</article>

<nav class="pager">
  <span class="wide">PREV</span><span>1</span><span>2</span><span>3</span><span>4</span><span>5</span><span>6</span><span>…</span><span>22</span><span class="wide">NEXT</span>
</nav>

<aside>
  <div class="ad" style="left:769px;top:155px;background:linear-gradient(180deg,#3a8a2a,#5cb040 60%,#2a6a20);border:2px solid #2a5a1a" role="img" aria-label="Conference advertisement banner"></div>

  <h2 class="side-heading" style="top:450px">TOP IMAGES</h2>
  <div class="thumb-item" style="top:516px"><div class="thumb" role="img" aria-label="Thumbnail of a painted mask" style="background:linear-gradient(135deg,#c89a20,#8a3010)"></div><span class="thumb-title">HOW TO TAKE BETTER SELFIES</span><span class="thumb-date">22-10-2013</span></div>
  <div class="thumb-item" style="top:653px"><div class="thumb" role="img" aria-label="Thumbnail of a phone in hand" style="background:linear-gradient(135deg,#e8d070,#c09060)"></div><span class="thumb-title">HOW TO TAKE BETTER SELFIES</span><span class="thumb-date">22-10-2013</span></div>
  <div class="thumb-item" style="top:788px"><div class="thumb" role="img" aria-label="Thumbnail portrait photo" style="background:linear-gradient(135deg,#c08060,#6a5040)"></div><span class="thumb-title">HOW TO TAKE BETTER SELFIES</span><span class="thumb-date">22-10-2013</span></div>
  <div class="thumb-item" style="top:921px"><div class="thumb" role="img" aria-label="Thumbnail of a city skyline at night" style="background:linear-gradient(180deg,#1a2a4a,#0a1020)"></div><span class="thumb-title">HOW TO TAKE BETTER SELFIES</span><span class="thumb-date">22-10-2013</span></div>
  <div class="thumb-item" style="top:1056px"><div class="thumb" role="img" aria-label="Thumbnail of a fiery horse artwork" style="background:linear-gradient(135deg,#f0a020,#a02008)"></div><span class="thumb-title">HOW TO TAKE BETTER SELFIES</span><span class="thumb-date">22-10-2013</span></div>
  <span class="view-more" style="top:1168px">VIEW MORE</span>

  <div class="ad" style="left:766px;top:1213px;background:linear-gradient(180deg,#1a5a9a,#1a4a88 80%,#7ab040)" role="img" aria-label="Public safety drill advertisement banner"></div>

  <h2 class="side-heading" style="top:1480px">TOP IMAGES</h2>
  <div class="thumb-item" style="top:1540px"><div class="thumb" role="img" aria-label="Thumbnail of goldfish bowls" style="background:linear-gradient(180deg,#e8f0f4,#8ac0d8)"></div><span class="thumb-title">HOW TO TAKE BETTER SELFIES</span><span class="thumb-date">22-10-2013</span></div>
  <div class="thumb-item" style="top:1677px"><div class="thumb" role="img" aria-label="Thumbnail of colourful abstract art" style="background:linear-gradient(135deg,#3a2a6a,#30a080)"></div><span class="thumb-title">HOW TO TAKE BETTER SELFIES</span><span class="thumb-date">22-10-2013</span></div>
  <div class="thumb-item" style="top:1814px"><div class="thumb" role="img" aria-label="Thumbnail of a clownfish in anemone" style="background:linear-gradient(135deg,#3a8a30,#e07020)"></div><span class="thumb-title">HOW TO TAKE BETTER SELFIES</span><span class="thumb-date">22-10-2013</span></div>
  <div class="thumb-item" style="top:1948px"><div class="thumb" role="img" aria-label="Thumbnail of a street scene" style="background:linear-gradient(180deg,#d0d8e0,#8a7060)"></div><span class="thumb-title">HOW TO TAKE BETTER SELFIES</span><span class="thumb-date">22-10-2013</span></div>
  <span class="view-more" style="top:2066px">VIEW MORE</span>

  <h2 class="side-heading" style="top:2124px">GET THE APP</h2>
  <div class="store-badge" style="top:2178px"></div>
  <div class="store-badge" style="top:2248px"></div>
</aside>

<footer class="site-footer">
  <div class="footer-nav">HOME | ABOUT US | SHARE | POST IMAGES | COMMENTS</div>
  <div class="copyright">COPYRIGHT ©2013 COMPANY NAME - ALL RIGHTS RESERVED</div>
</footer>

</body>
</html>
```